Building company needs a new logo and letterhead design

We need a new and refreshed logo and letterhead design for an existing building company. We specialise in residential as well as commercial building/construction, design and project management. Our company name is Talvek Constructions Pty Ltd. Our primary colours that we want to use are black/orange/white. We do renovations/alterations/new homes both residential and commercial. We are a medium sized building company. We want something simple and modern.

Industry/Entity Type

Residential

```html
<!DOCTYPE html>
<html lang="en">
<head>
<meta charset="utf-8">
<title>Talvek Constructions Pty Ltd – Letterhead</title>
<link rel="stylesheet" href="https://fonts.googleapis.com/css2?family=Didact+Gothic&display=swap">
<style>
  :root {
    --canvas: #ffffff;
    --paper: #ffffff;
    --orange: #f08a24;
    --orange-light: #f7b36a;
    --ink: #3a3a3a;
    --charcoal: #2b2b2b;
    --watermark: #fbf1e4;
    --page-edge: #e6e6e6;
  }
  * { box-sizing: border-box; margin: 0; padding: 0; }
  html, body { width: 1200px; height: 900px; overflow: hidden; background: var(--canvas); }
  body { position: relative; font-family: "Didact Gothic", "Century Gothic", sans-serif; color: var(--ink); }

  .letterhead {
    position: absolute; left: 320px; top: 55px; width: 560px; height: 790px;
    background: var(--paper);
    box-shadow: 0 0 0 1px var(--page-edge), 2px 3px 6px rgba(0,0,0,0.08);
    overflow: hidden;
  }

  .brand-mark {
    position: absolute; left: 54px; top: 54px; width: 40px; height: 40px;
    background: var(--orange);
  }
  .brand-divider {
    position: absolute; left: 120px; top: 45px; width: 2px; height: 52px;
    background: var(--orange);
  }
  .company-name {
    position: absolute; left: 133px; top: 61px;
    font-size: 15.5px; font-weight: 400; letter-spacing: 0.1px; color: var(--charcoal);
    white-space: nowrap;
  }

  .contact-list {
    position: absolute; left: 388px; top: 45px; list-style: none;
    font-size: 9px; line-height: 10.4px; color: var(--ink);
  }
  .contact-list li { display: flex; align-items: center; gap: 3px; white-space: nowrap; }
  .contact-list svg { width: 7px; height: 7px; flex: none; }
  .contact-list .web { color: var(--orange); }

  .header-rule {
    position: absolute; left: 0; top: 101px; width: 560px; height: 4px;
    background: linear-gradient(to right, var(--orange), var(--orange-light) 50%, var(--orange));
  }

  .watermark {
    position: absolute; right: 30px; top: 560px;
    font-size: 104px; font-weight: 400; line-height: 1; letter-spacing: 2px;
    color: var(--watermark); white-space: nowrap; user-select: none;
  }

  .footer-address {
    position: absolute; left: 0; top: 755px; width: 560px; text-align: center;
    font-size: 9px; color: var(--ink); word-spacing: 1px;
  }
  .footer-rule {
    position: absolute; left: 0; top: 772px; width: 560px; height: 4px;
    background: linear-gradient(to right, #8a8a8a, var(--charcoal) 30%, var(--charcoal) 70%, #8a8a8a);
  }
</style>
</head>
<body>
  <main class="letterhead">
    <div class="brand-mark"></div>
    <div class="brand-divider"></div>
    <h1 class="company-name">TALVEK CONSTRUCTIONS PTY LTD.</h1>

    <ul class="contact-list">
      <li><svg viewBox="0 0 8 8"><path d="M2 0.5 L3.4 2.4 L2.6 3.3 Q3.6 5 5 5.6 L5.8 4.8 L7.6 6 L6.6 7.5 Q1.5 6.5 0.5 1.4 Z" fill="var(--orange)"/></svg>0291004217</li>
      <li><svg viewBox="0 0 8 8"><rect x="0.5" y="3" width="7" height="4" rx="1" fill="var(--orange)"/><rect x="2" y="0.8" width="4" height="2.4" fill="var(--orange)"/></svg>0291004218</li>
      <li><svg viewBox="0 0 8 8"><rect x="2" y="0.5" width="4" height="7" rx="0.8" fill="var(--orange)"/><rect x="2.8" y="1.4" width="2.4" height="4" fill="#fff"/></svg>0400123987</li>
      <li><svg viewBox="0 0 8 8"><rect x="0.5" y="1.5" width="7" height="5" fill="var(--orange)"/><path d="M0.5 1.5 L4 4.4 L7.5 1.5" stroke="#fff" stroke-width="0.7" fill="none"/></svg>office@talvekmail.com</li>
      <li class="web"><svg viewBox="0 0 8 8"><circle cx="4" cy="4" r="3.5" fill="var(--orange)"/><path d="M0.5 4 H7.5 M4 0.5 V7.5" stroke="#fff" stroke-width="0.6"/></svg>www.talvekconstructions.com.au</li>
    </ul>

    <div class="header-rule"></div>

    <div class="watermark" aria-hidden="true">TALVEK</div>

    <p class="footer-address">PO Box 512 • Marlow Heights NSW 2199</p>
    <div class="footer-rule"></div>
  </main>
</body>
</html>
```